Need a very flashy Referral Bonus Business Card to be able to pass out

Would like to create a business card that is able to be passed out to employees for them to pass to their referral candidataes who are looking for jobs; so they can easily take the card to one of our offices to apply for jobs. They will need to have our logo and something about Referral Bonuse; and on the flip side our phone numbers for offices; and place for the employee to put his/her name and the candidate being referred to put his or her name as well.

Target Market(s)

For our current Employees and candidates looking for jobs.

Industry/Entity Type

Business

Contact Information for Business Card

Logo on at least 1 side of business card. Then the other side; Employee name, Referral Candidate Name: Would like for it to list Addison:614-583-2047/Irving: 614-377-8406/Denton- 517-826-3914

Font styles to use
Sans Serif

Colors
ec1f27

Requirements
Must have
• Must have place for the employee to write his or her name and a place for the person being referred to write his or her name as well. As well as office contact numbers: Addison:614-583-2047/Irving: 614-377-8406/Denton- 517-826-3914 and www.brivelworks.example
Nice to have
• NA
Should not have
• NA

```html
<!DOCTYPE html>
<html lang="en">
<head>
<meta charset="utf-8">
<title>Brivelworks Referral Card</title>
<link rel="stylesheet" href="https://fonts.googleapis.com/css2?family=Open+Sans:wght@400;600;700&display=swap">
<style>
  :root {
    --brand-red: #ec1f27;
    --ink: #1a1a1a;
    --card: #ffffff;
    --backdrop: #2a2a2a;
    --rule: #222222;
  }
  * { margin: 0; padding: 0; box-sizing: border-box; }
  html, body {
    width: 1200px; height: 852px; overflow: hidden;
    background: var(--backdrop);
    font-family: "Open Sans", Arial, sans-serif;
  }
  .stage {
    position: relative; width: 1200px; height: 852px;
    display: flex; align-items: center; justify-content: center; gap: 40px;
  }
  .card {
    position: relative; width: 540px; height: 309px;
    background: var(--card); border-radius: 22px; overflow: hidden;
    box-shadow: 0 10px 30px rgba(0,0,0,.45);
  }
  .card-lines { position: absolute; inset: 0; }
  .wordmark {
    position: absolute; color: var(--brand-red);
    font-weight: 700; letter-spacing: -0.5px; line-height: 1;
  }
  .card-front .wordmark {
    font-size: 54px; left: 0; right: 0; top: 120px; text-align: center;
  }
  .card-back .wordmark { font-size: 40px; right: 34px; top: 118px; }

  .referral-fields { position: absolute; left: 34px; top: 40px; width: 480px; }
  .field {
    display: flex; align-items: flex-end; gap: 8px;
    font-size: 13px; color: var(--ink); margin-bottom: 22px;
  }
  .field-line { flex: 1; border-bottom: 1px solid var(--rule); height: 14px; }

  .office-list {
    position: absolute; left: 34px; top: 170px;
    list-style: none; font-size: 14px; line-height: 19px; color: var(--ink);
  }
  .office-name { color: var(--brand-red); }
  .website { font-size: 15px; }
</style>
</head>
<body>
<main class="stage">

  <section class="card card-front" aria-label="Card front">
    <svg class="card-lines" width="540" height="309" viewBox="0 0 540 309">
      <g stroke="#ec1f27" fill="none" stroke-width="3">
        <line x1="28" y1="46" x2="540" y2="46"/>
        <polyline points="44,36 28,46 44,56"/>
        <line x1="0" y1="250" x2="512" y2="250"/>
        <polyline points="496,240 512,250 496,260"/>
        <line x1="0" y1="282" x2="540" y2="282" stroke-width="5"/>
      </g>
    </svg>
    <div class="wordmark">Brivelworks</div>
  </section>

  <section class="card card-back" aria-label="Card back">
    <svg class="card-lines" width="540" height="309" viewBox="0 0 540 309">
      <line x1="0" y1="280" x2="540" y2="280" stroke="#ec1f27" stroke-width="5"/>
    </svg>

    <div class="referral-fields">
      <div class="field"><span>Employee name</span><span class="field-line"></span></div>
      <div class="field"><span>Referral Candidate Name</span><span class="field-line"></span></div>
    </div>

    <div class="wordmark">Brivelworks</div>

    <ul class="office-list">
      <li><span class="office-name">Addison</span> : 614-583-2047</li>
      <li><span class="office-name">Irving</span> : 614-377-8406</li>
      <li><span class="office-name">Denton</span> : 517-826-3914</li>
      <li><span class="office-name">Oklahoma City</span> : 405-730-5168</li>
      <li class="website">www.brivelworks.example</li>
    </ul>
  </section>

</main>
</body>
</html>
```